Ambulance Full Vehicle Wrap - Local Roof Cleaning Business

I need a full vehicle wrap design for a 2003 K370 ambulance. Attached are photos with dimensions and the logo file. Also, I've attached a rough mock-up of one concept, but I'm open to new ideas. I need the design to include:

Phone: 877-4-TOVELIK
Website: tovelikroof.com
"Always Clean Guarantee"
"Safe for Roofs, Pets, and Plants"

Font styles to use
Sans Serif

```html
<!DOCTYPE html>
<html lang="en">
<head>
<meta charset="utf-8">
<title>Tovelik Roof – Vehicle Wrap Layout</title>
<link rel="stylesheet" href="https://fonts.googleapis.com/css2?family=Barlow+Condensed:ital,wght@1,600&family=Oswald:wght@500;700&family=Open+Sans:wght@700&display=swap">
<style>
  :root {
    --wrap-blue: #1b5fae;
    --wrap-navy: #1f3a78;
    --wrap-deep: #1d3470;
    --wrap-red: #dc1f2f;
    --wrap-dark-red: #a61d27;
    --wrap-white: #ffffff;
    --wrap-grey: #c9ccd3;
    --stage-dark: #2d2d2f;
    --label-ink: #111111;
  }
  * { box-sizing: border-box; }
  html, body {
    margin: 0;
    width: 1200px;
    height: 2503px;
    overflow: hidden;
    background: var(--wrap-white);
  }
  .board { position: relative; width: 1200px; height: 2503px; }
  .vehicle-stage {
    position: absolute; left: 64px; top: 70px; width: 1067px; height: 534px;
    background: var(--stage-dark);
  }
  .vehicle-render {
    position: absolute; left: 30px; top: 70px; width: 1010px; height: 420px;
    border-radius: 40px 12px 30px 30px;
    background: linear-gradient(100deg, var(--wrap-navy) 0%, var(--wrap-blue) 45%, var(--wrap-deep) 100%);
  }
  .panel { position: absolute; display: block; }
  .panel-side { left: 60px; top: 685px; width: 1076px; height: 484px; }
  .panel-back { left: 294px; top: 1303px; width: 606px; height: 483px; }
  .panel-door { left: 331px; top: 1938px; width: 534px; height: 407px; }
  .panel-label {
    position: absolute; left: 0; width: 1200px; margin: 0;
    text-align: center;
    font-family: "Open Sans", Arial, sans-serif;
    font-weight: 700; font-size: 31px; color: var(--label-ink);
    letter-spacing: 0.5px;
  }
  .label-side { top: 1186px; }
  .label-back { top: 1823px; }
  .label-door { top: 2386px; }
  .slogan { font-family: "Barlow Condensed", "Arial Narrow", sans-serif; font-style: italic; font-weight: 600; }
  .contact { font-family: "Oswald", "Arial Narrow", sans-serif; font-weight: 500; }
  .brand-name { font-family: "Oswald", "Arial Narrow", sans-serif; font-weight: 700; }
</style>
</head>
<body>
<main class="board">

  <section class="vehicle-stage">
    <div class="vehicle-render" role="img" aria-label="Side view of the K370 ambulance with the blue, red and white wrap applied"></div>
  </section>

  <!-- Side panel -->
  <svg class="panel panel-side" viewBox="0 0 1112 500" preserveAspectRatio="none" aria-label="Side panel">
    <defs>
      <linearGradient id="sideBase" x1="0" y1="0" x2="1" y2="1">
        <stop offset="0" stop-color="#1b62b0"/>
        <stop offset="1" stop-color="#1d3470"/>
      </linearGradient>
      <radialGradient id="sideGlow" cx="780" cy="210" r="330" gradientUnits="userSpaceOnUse">
        <stop offset="0" stop-color="#e6f0ff" stop-opacity="0.9"/>
        <stop offset="0.35" stop-color="#7fa6dc" stop-opacity="0.55"/>
        <stop offset="1" stop-color="#1d3470" stop-opacity="0"/>
      </radialGradient>
    </defs>
    <rect width="1112" height="500" fill="url(#sideBase)"/>
    <rect width="1112" height="500" fill="url(#sideGlow)"/>
    <path d="M118,500 C260,300 600,170 990,0 L1040,0 C640,190 300,320 160,500 Z" fill="var(--wrap-grey)"/>
    <path d="M130,500 C270,305 610,175 1000,0 L1030,0 C640,190 300,320 160,500 Z" fill="var(--wrap-white)"/>
    <path d="M215,500 C330,330 640,210 1070,0 L1112,0 L1112,40 C700,235 380,350 300,500 Z" fill="var(--wrap-red)"/>
    <path d="M255,500 C360,350 650,235 1112,25 L1112,40 C700,235 380,350 300,500 Z" fill="var(--wrap-dark-red)"/>
    <path d="M355,500 C420,400 520,330 650,295 C545,345 465,415 395,500 Z" fill="var(--wrap-white)"/>
    <path d="M460,455 C650,420 850,330 1010,255 C860,360 690,435 460,455 Z" fill="var(--wrap-red)"/>
    <path d="M470,487 C700,472 950,400 1112,290 L1112,330 C950,435 720,485 470,487 Z" fill="var(--wrap-white)"/>
    <path d="M770,500 C900,472 1030,420 1112,370 L1112,425 C1045,462 935,492 865,500 Z" fill="var(--wrap-white)"/>
    <text class="slogan" x="228" y="112" text-anchor="middle" font-size="50" fill="var(--wrap-white)">ALWAYS</text>
    <text class="slogan" x="228" y="160" text-anchor="middle" font-size="50" fill="var(--wrap-white)">CLEAN GUARANTEE</text>
    <rect x="80" y="176" width="300" height="3" fill="var(--wrap-red)"/>
    <text class="brand-name" x="780" y="195" text-anchor="middle" font-size="92" fill="var(--wrap-white)">TOVELIK</text>
    <text class="brand-name" x="780" y="290" text-anchor="middle" font-size="92" fill="var(--wrap-white)">ROOF</text>
  </svg>
  <p class="panel-label label-side">SIDE&nbsp; 169” X 76”</p>

  <!-- Back panel -->
  <svg class="panel panel-back" viewBox="0 0 626 500" preserveAspectRatio="none" aria-label="Back panel">
    <defs>
      <radialGradient id="backGlow" cx="318" cy="130" r="260" gradientUnits="userSpaceOnUse">
        <stop offset="0" stop-color="#dbe7fb" stop-opacity="0.85"/>
        <stop offset="0.4" stop-color="#5f86c4" stop-opacity="0.45"/>
        <stop offset="1" stop-color="#1f3a78" stop-opacity="0"/>
      </radialGradient>
    </defs>
    <rect width="626" height="500" fill="var(--wrap-navy)"/>
    <rect width="626" height="500" fill="url(#backGlow)"/>
    <path d="M0,310 C10,390 70,450 130,480 C70,460 20,420 0,360 Z" fill="var(--wrap-white)"/>
    <path d="M0,395 C40,450 110,480 180,500 L90,500 C50,480 15,455 0,440 Z" fill="var(--wrap-red)"/>
    <path d="M0,440 C20,460 60,485 90,500 L40,500 C25,490 10,480 0,475 Z" fill="var(--wrap-dark-red)"/>
    <path d="M0,485 C10,490 20,495 30,500 L0,500 Z" fill="var(--wrap-white)"/>
    <text class="brand-name" x="318" y="118" text-anchor="middle" font-size="54" fill="var(--wrap-white)">TOVELIK</text>
    <text class="brand-name" x="318" y="178" text-anchor="middle" font-size="54" fill="var(--wrap-white)">ROOF</text>
    <circle cx="60" cy="270" r="14" fill="var(--wrap-white)"/>
    <path d="M54,262 l4,-2 l3,5 l-2,2 q2,4 6,6 l2,-2 l5,3 l-2,4 q-12,-2 -16,-16 Z" fill="var(--wrap-navy)"/>
    <text class="contact" x="90" y="281" font-size="30" fill="var(--wrap-red)">877-4-TOVELIK</text>
    <circle cx="380" cy="270" r="14" fill="none" stroke="var(--wrap-white)" stroke-width="2.5"/>
    <ellipse cx="380" cy="270" rx="6" ry="14" fill="none" stroke="var(--wrap-white)" stroke-width="2"/>
    <line x1="366" y1="270" x2="394" y2="270" stroke="var(--wrap-white)" stroke-width="2"/>
    <text class="contact" x="405" y="281" font-size="30" fill="var(--wrap-red)">tovelikroof.com</text>
    <text class="slogan" x="318" y="382" text-anchor="middle" font-size="34" fill="var(--wrap-white)">ALWAYS CLEAN GUARANTEE</text>
    <rect x="200" y="392" width="236" height="2" fill="var(--wrap-red)"/>
    <text class="contact" x="318" y="432" text-anchor="middle" font-size="29" fill="var(--wrap-red)">SAFE FOR ROOFS, PETS, AND PLANTS</text>
  </svg>
  <p class="panel-label label-back">BACK&nbsp; 95” X 76”</p>

  <!-- Door panel -->
  <svg class="panel panel-door" viewBox="0 0 552 420" preserveAspectRatio="none" aria-label="Door panel">
    <defs>
      <linearGradient id="doorBase" x1="0" y1="0" x2="1" y2="0.4">
        <stop offset="0" stop-color="#1b62b0"/>
        <stop offset="1" stop-color="#1f3470"/>
      </linearGradient>
    </defs>
    <rect width="552" height="420" fill="url(#doorBase)"/>
    <path d="M0,280 C110,240 230,270 330,420 L305,420 C220,300 120,270 0,300 Z" fill="var(--wrap-grey)"/>
    <path d="M0,285 C110,248 225,275 320,420 L300,420 C215,305 120,275 0,300 Z" fill="var(--wrap-white)"/>
    <path d="M30,270 C130,265 220,330 285,420 L220,420 C170,350 110,300 30,270 Z" fill="var(--wrap-red)"/>
    <path d="M0,330 C70,340 140,380 175,420 L110,420 C80,390 40,360 0,345 Z" fill="var(--wrap-red)"/>
    <path d="M100,290 C160,310 210,360 240,420 L225,420 C195,365 150,320 100,290 Z" fill="var(--wrap-dark-red)"/>
    <path d="M0,375 C30,390 60,405 80,420 L0,420 Z" fill="var(--wrap-white)"/>
    <circle cx="308" cy="290" r="14" fill="var(--wrap-white)"/>
    <path d="M302,282 l4,-2 l3,5 l-2,2 q2,4 6,6 l2,-2 l5,3 l-2,4 q-12,-2 -16,-16 Z" fill="var(--wrap-blue)"/>
    <text class="contact" x="333" y="300" font-size="26" fill="var(--wrap-red)">877-4-TOVELIK</text>
    <circle cx="308" cy="333" r="13" fill="none" stroke="var(--wrap-white)" stroke-width="2.5"/>
    <ellipse cx="308" cy="333" rx="5.5" ry="13" fill="none" stroke="var(--wrap-white)" stroke-width="2"/>
    <line x1="295" y1="333" x2="321" y2="333" stroke="var(--wrap-white)" stroke-width="2"/>
    <text class="contact" x="331" y="343" font-size="26" fill="var(--wrap-red)">tovelikroof.com</text>
  </svg>
  <p class="panel-label label-door">DOOR&nbsp; 95” X 76”</p>

</main>
</body>
</html>
```